Website design for staffing/workforce solutions company - Halvard Staffing Solutions

Create a launch-ready website
Halvard Staffing Solutions also known as HSS. This is a company that specializes in Staffing/Work force solutions for Healthcare/IT/Logistics/Maintenance/Construction/Manufacturing/Industrial/General Labor. HSS works with government agencies/contracts also. Use the attached logo in the build of the website. Website should be clean, modern, engaging, innovative. Website needs to speak to the professional services industry.
Halvard Staffing Solutions or HSS is a certified VOSB, SDVOSB, DBE and Minority-Owned Business.
The website needs to be compliant for government contracting.

Website needs to include the following--
Modern UI/UX Enhancements: A hero section with a strong call-to-action.
Government Contracting Compliance: Certification display and a Capability Statement download.
Advanced Careers Section: A dedicated job application portal.
Social Media & Lead Generation: Links to Profilary, Quillo, and Mingleo.
Security & Performance: Optimized for SEO, fast loading, and mobile responsiveness.
1. Modern Design Upgrades
๐Ÿ”น Upgrade UI/UX for a Professional, Trustworthy Look
โœ… Full-width hero banner with a high-quality background image representing business, technology, and workforce solutions.
โœ… Animated elements (subtle transitions for smooth browsing experience).
โœ… Bold CTA buttons for easy navigation to key actions (e.g., โ€œGet Startedโ€ or โ€œRequest a Consultationโ€).
โœ… Dark-themed header with contrasting colors (professional & government-trustworthy).
โœ… New Homepage Hero Section Example:
"Your Trusted Partner in Workforce, IT, Maintenance & Logistics Solutions"
Button: "Discover Our Services"

2. Enhanced Government Contracting Section (Key for Compliance)
๐Ÿ“Œ Essential for securing contracts & building credibility
โœ… Capability Statement (Downloadable PDF)

Showcase key past contracts, company qualifications, and services in a downloadable format for government buyers.
โœ… Certifications Display (VOSB, SDVOSB, DBE, Minority-Owned Business)

Visual badge display to emphasize legitimacy for government contracts.
โœ… Procurement Readiness Details

NAICS Codes, DUNS Number, CAGE Code, and relevant VPR.example registration details.
โœ… Past Performance Showcase (Case Studies Section)

Highlight successful projects and government contracts.
โœ… Compliance & Security

Add SOC 2, HIPAA (for healthcare staffing), and ITAR compliance if applicable.
3. Advanced Job Search & Candidate Portal (For Staffing Services)
๐Ÿ“Œ To attract top talent for staffing contracts

โœ… Advanced Job Search Feature

Filters: Industry, location, job type (contract/full-time), salary range, and clearance level (for government jobs).
โœ… Candidate Login Portal

Applicants can upload resumes, track applications, and receive job alerts.
โœ… Employer Portal (For Businesses Hiring Through HSS)

A dedicated section for companies to submit staffing requests and view candidate matches.
4. Service-Specific Landing Pages (SEO & Engagement)
๐Ÿ“Œ Helps different industries find relevant services faster

๐Ÿ”น Dedicated Pages for Each Service:
โœ… Staffing & Workforce Solutions

Specialized sections for Healthcare, IT, Construction, Industrial, and General Labor staffing.
โœ… IT Services

List services like Cybersecurity, Cloud Solutions, and IT Consulting.
Showcase tech stack & certifications.
โœ… Logistics & Maintenance

Detail fleet management, supply chain services, and industrial maintenance.
โœ… Government Contracting Solutions

A streamlined page for government agencies.
5. Security & Compliance Upgrades (For Government Work)
๐Ÿ“Œ To ensure compliance & credibility in government contracting

โœ… SSL Certification (100% Required for Security)

Secure client and job applicant data.
โœ… ADA Compliance (Accessibility)

Ensure the website follows WCAG 2.1 accessibility standards for government clients.
โœ… GDPR & Data Protection Features

A privacy policy and terms of service to comply with data regulations.
6. Performance & Mobile Optimization
๐Ÿ“Œ To ensure fast loading & responsiveness

โœ… Mobile-Responsive Design

Optimized for mobile-friendly navigation since many users browse from phones.
โœ… Fast-Loading Pages

Optimize images & implement lazy loading for better site speed.
โœ… SEO-Optimized Pages

Improve search ranking on Searvo with:
Keyword-optimized content (e.g., โ€œGovernment Contracting Staffing Servicesโ€)
Schema markup for job listings
Blog/articles about staffing trends
7. Social Media & Lead Generation
๐Ÿ“Œ For brand credibility & client engagement

โœ… Profilary, Quillo, Mingleo Integration

Display recent updates from Profilary (primary for B2B & government).
โœ… Lead Capture Forms

Forms for business inquiries, talent applications, and government RFPs.
โœ… Client & Candidate Testimonials
Showcase client success stories & employee experiences

Good websites to pull examples for inspiration/direction--
https://www.pelmora.example/
https://www.tovrinex.example/
https://brambleworks.example/homepage/
https://www.quantelvetting.example/capability-statement

Staffing/Professional Services

Coded - Design and coding required

5+ page

• Website needs to include the following-- Modern UI/UX Enhancements: A hero section with a strong call-to-action. Government Contracting Compliance: Certification display and a Capability Statement download. Advanced Careers Section: A dedicated job application portal. Social Media & Lead Generation: Links to Profilary, Quillo, and Mingleo. Security & Performance: Optimized for SEO, fast loading, and mobile responsiveness. 1. Modern Design Upgrades ๐Ÿ”น Upgrade UI/UX for a Professional, Trustworthy Look โœ… Full-width hero banner with a high-quality background image representing business, technology, and workforce solutions. โœ… Animated elements (subtle transitions for smooth browsing experience). โœ… Bold CTA buttons for easy navigation to key actions (e.g., โ€œGet Startedโ€ or โ€œRequest a Consultationโ€). โœ… Dark-themed header with contrasting colors (professional & government-trustworthy). โœ… New Homepage Hero Section Example: "Your Trusted Partner in Workforce, IT, & Logistics Solutions" Button: "Discover Our Services" 2. Enhanced Government Contracting Section (Key for Compliance) ๐Ÿ“Œ Essential for securing contracts & building credibility โœ… Capability Statement (Downloadable PDF) Showcase key past contracts, company qualifications, and services in a downloadable format for government buyers. โœ… Certifications Display (VOSB, SDVOSB, DBE, Minority-Owned Business) Visual badge display to emphasize legitimacy for government contracts. โœ… Procurement Readiness Details NAICS Codes, DUNS Number, CAGE Code, and relevant VPR.example registration details. โœ… Past Performance Showcase (Case Studies Section) Highlight successful projects and government contracts. โœ… Compliance & Security Add SOC 2, HIPAA (for healthcare staffing), and ITAR compliance if applicable. 3. Advanced Job Search & Candidate Portal (For Staffing Services) ๐Ÿ“Œ To attract top talent for staffing contracts โœ… Advanced Job Search Feature Filters: Industry, location, job type (contract/full-time), salary range, and clearance level (for government jobs). โœ… Candidate Login Portal Applicants can upload resumes, track applications, and receive job alerts. โœ… Employer Portal (For Businesses Hiring Through HSS) A dedicated section for companies to submit staffing requests and view candidate matches. 4. Service-Specific Landing Pages (SEO & Engagement) ๐Ÿ“Œ Helps different industries find relevant services faster ๐Ÿ”น Dedicated Pages for Each Service: โœ… Staffing & Workforce Solutions Specialized sections for Healthcare, IT, Construction, Industrial, and General Labor staffing. โœ… IT Services List services like Cybersecurity, Cloud Solutions, and IT Consulting. Showcase tech stack & certifications. โœ… Logistics & Maintenance Detail fleet management, supply chain services, and industrial maintenance. โœ… Government Contracting Solutions A streamlined page for government agencies. 5. Security & Compliance Upgrades (For Government Work) ๐Ÿ“Œ To ensure compliance & credibility in government contracting โœ… SSL Certification (100% Required for Security) Secure client and job applicant data. โœ… ADA Compliance (Accessibility) Ensure the website follows WCAG 2.1 accessibility standards for government clients. โœ… GDPR & Data Protection Features A privacy policy and terms of service to comply with data regulations. 6. Performance & Mobile Optimization ๐Ÿ“Œ To ensure fast loading & responsiveness โœ… Mobile-Responsive Design Optimized for mobile-friendly navigation since many users browse from phones. โœ… Fast-Loading Pages Optimize images & implement lazy loading for better site speed. โœ… SEO-Optimized Pages Improve search ranking on Searvo with: Keyword-optimized content (e.g., โ€œGovernment Contracting Staffing Servicesโ€) Schema markup for job listings Blog/articles about staffing trends 7. Social Media & Lead Generation ๐Ÿ“Œ For brand credibility & client engagement โœ… Profilary, Quillo, Mingleo Integration Display recent updates from Profilary (primary for B2B & government). โœ… Lead Capture Forms Forms for business inquiries, talent applications, and government RFPs. โœ… Client & Candidate Testimonials Showcase client success stories & employee experiences Good websites to pull examples for inspiration/direction-- https://www.pelmora.example/ https://www.tovrinex.example/ https://brambleworks.example/homepage/

```html
<!DOCTYPE html>
<html lang="en">
<head>
<meta charset="utf-8">
<title>Halvard Staffing Solutions</title>
<link href="https://fonts.googleapis.com/css2?family=Ubuntu:wght@300;400;500;700&display=swap" rel="stylesheet">
<style>
:root{
  --header:#121a30;
  --hero-a:#1f2f6e;
  --hero-b:#2c4aa8;
  --hero-c:#25378a;
  --blue:#1d5cf5;
  --sky:#4a9cf5;
  --cyan:#3cc8ee;
  --stat:#5aa8f7;
  --ink:#111827;
  --body:#4b5563;
  --muted:#6b7280;
  --page:#f7f9fc;
  --card:#ffffff;
  --icon-bg:#e3edfe;
  --green:#22c55e;
}
*{margin:0;padding:0;box-sizing:border-box}
html,body{width:826px;height:1200px;overflow:hidden}
body{font-family:"Ubuntu",sans-serif;background:var(--page);color:var(--ink);position:relative}
.site-header{position:absolute;left:0;top:0;width:826px;height:56px;background:var(--header);z-index:3}
.brand{position:absolute;left:116px;top:20px;color:#fff;font-size:10px;font-weight:500;letter-spacing:.3px}
.main-nav{position:absolute;top:22px;left:0;width:100%;font-size:8.3px;color:#fff}
.main-nav a{position:absolute;color:#fff;text-decoration:none;white-space:nowrap}
.btn-start{position:absolute;left:662px;top:19px;width:52px;height:18px;background:var(--blue);color:#fff;border-radius:3px;font-size:7px;font-weight:500;display:flex;align-items:center;justify-content:center}
.hero{position:absolute;left:0;top:56px;width:826px;height:452px;background:linear-gradient(120deg,var(--hero-a) 0%,var(--hero-b) 45%,#3156b8 65%,var(--hero-c) 100%)}
.hero-photo{position:absolute;inset:0;background:radial-gradient(ellipse at 70% 30%,rgba(120,140,200,.35),transparent 60%),radial-gradient(ellipse at 15% 70%,rgba(160,170,210,.25),transparent 55%)}
.cert-pill{position:absolute;left:107px;top:65px;width:170px;height:18px;border:1px solid rgba(120,160,255,.5);background:rgba(30,50,130,.45);border-radius:9px;color:#cfe0ff;font-size:6.9px;display:flex;align-items:center;padding-left:9px;gap:5px}
.hero-title{position:absolute;left:107px;top:94px;font-size:30px;font-weight:700;line-height:37.5px;color:#fff}
.hero-title .accent{background:linear-gradient(90deg,var(--sky),var(--cyan));-webkit-background-clip:text;background-clip:text;color:transparent}
.hero-lead{position:absolute;left:107px;top:212px;width:285px;font-size:10.4px;font-weight:300;line-height:16.5px;color:#e6ecff}
.stat{position:absolute;top:307px;width:90px;text-align:center;margin-left:-45px}
.stat b{display:block;font-size:15.5px;font-weight:700;color:var(--stat);line-height:18px}
.stat span{font-size:7px;color:#b7c3e6}
.hero-btn{position:absolute;top:368px;height:20px;border-radius:3px;font-size:7.2px;font-weight:500;display:flex;align-items:center;justify-content:center;gap:8px}
.btn-primary{left:107px;width:101px;background:var(--blue);color:#fff}
.btn-light{left:215px;width:93px;background:#fff;color:var(--blue)}
.solutions-card{position:absolute;left:423px;top:168px;width:291px;height:116px;border:1px solid rgba(160,185,255,.35);background:rgba(70,95,190,.35);border-radius:7px}
.orb{position:absolute;border-radius:50%;background:rgba(90,130,230,.45)}
.card-icon{position:absolute;left:16px;top:16px;width:24px;height:24px;border-radius:5px;background:var(--blue);display:flex;align-items:center;justify-content:center}
.card-head{position:absolute;left:48px;top:18px;color:#fff}
.card-head h3{font-size:8px;font-weight:500}
.card-head p{font-size:6.6px;color:#c9d5f5;margin-top:2px}
.card-list{position:absolute;left:16px;top:53px;width:259px;list-style:none}
.card-list li{display:flex;justify-content:space-between;align-items:center;height:18px;font-size:6.8px;color:#fff}
.card-list li::after{content:"";width:4px;height:4px;border-radius:50%;background:var(--green)}
.services-title{position:absolute;top:548px;width:100%;text-align:center;font-size:17.6px;font-weight:700}
.services-lead{position:absolute;top:577px;left:213px;width:400px;text-align:center;font-size:10px;line-height:14.5px;color:var(--body)}
.service-grid{position:absolute;left:107px;top:637px;width:607px;display:grid;grid-template-columns:repeat(4,142px);grid-template-rows:194px 181px;column-gap:13px;row-gap:13px}
.service{background:var(--card);border-radius:6px;box-shadow:0 1px 4px rgba(20,30,60,.08);padding:11px 12px 0;text-align:center}
.service .ico{width:32px;height:32px;margin:0 auto;border-radius:5px;background:var(--icon-bg);display:flex;align-items:center;justify-content:center}
.service h3{font-size:10px;font-weight:400;margin-top:18px;line-height:12px}
.service p{font-size:8px;font-weight:300;line-height:12px;color:var(--body);margin-top:21px}
.service ul{list-style:none;text-align:left;margin-top:8px}
.service li{font-size:6.9px;color:var(--muted);line-height:14px;padding-left:7px;position:relative}
.service li::before{content:"";position:absolute;left:0;top:5.5px;width:2.5px;height:2.5px;border-radius:50%;background:var(--blue)}
.gov-band{position:absolute;left:107px;top:1050px;width:607px;height:109px;background:var(--blue);border-radius:6px;text-align:center;color:#fff}
.gov-band h2{font-size:11.5px;font-weight:700;margin-top:17px}
.gov-band p{font-size:7.8px;font-weight:300;line-height:12px;width:340px;margin:8px auto 0;color:#e5edff}
.gov-btn{width:95px;height:17px;margin:10px auto 0;background:#fff;color:var(--blue);border-radius:3px;font-size:7px;font-weight:500;display:flex;align-items:center;justify-content:center;gap:8px}
svg{display:block}
</style>
</head>
<body>
<header class="site-header">
  <div class="brand">Halvard Staffing Solutions</div>
  <nav class="main-nav">
    <a style="left:323px">Home</a><a style="left:361px">Services</a><a style="left:405px">Certifications</a><a style="left:467px">Careers</a><a style="left:509px">Contact</a>
  </nav>
  <div class="btn-start">Get Started</div>
</header>

<section class="hero">
  <div class="hero-photo" role="img" aria-label="Photo of business professionals meeting in an office, blue tinted"></div>
  <div class="cert-pill">
    <svg width="7" height="7" viewBox="0 0 24 24" fill="none" stroke="#cfe0ff" stroke-width="2"><path d="M12 2l8 3v6c0 5-3.5 9-8 11-4.5-2-8-6-8-11V5z"/></svg>
    Government Certified • VOSB • SDVOSB • DBE
  </div>
  <h1 class="hero-title">Your Trusted Partner<br>in <span class="accent">Workforce</span><br><span class="accent">Solutions</span></h1>
  <p class="hero-lead">Delivering exceptional staffing and workforce solutions across Healthcare, IT, Logistics, Maintenance, Construction, Manufacturing, and Industrial sectors for both private and government clients.</p>
  <div class="stat" style="left:150px"><b>500+</b><span>Projects Completed</span></div>
  <div class="stat" style="left:252px"><b>10+</b><span>Years Experience</span></div>
  <div class="stat" style="left:355px"><b>24/7</b><span>Support Available</span></div>
  <div class="hero-btn btn-primary">Discover Our Services
    <svg width="7" height="7" viewBox="0 0 24 24" fill="none" stroke="#fff" stroke-width="2.5"><path d="M4 12h15M13 6l6 6-6 6"/></svg></div>
  <div class="hero-btn btn-light">Request Consultation</div>

  <div class="orb" style="left:675px;top:160px;width:48px;height:48px"></div>
  <div class="solutions-card">
    <div class="card-icon"><svg width="12" height="12" viewBox="0 0 24 24" fill="none" stroke="#fff" stroke-width="2"><rect x="6" y="3" width="12" height="18" rx="1"/><path d="M10 7h1M13 7h1M10 11h1M13 11h1M10 15h1M13 15h1M3 21h18"/></svg></div>
    <div class="card-head"><h3>Enterprise Solutions</h3><p>Scalable workforce management</p></div>
    <ul class="card-list"><li>Healthcare Staffing</li><li>IT Solutions</li><li>Government Contracts</li></ul>
  </div>
  <div class="orb" style="left:410px;top:263px;width:32px;height:32px;background:rgba(110,130,220,.4)"></div>
</section>

<h2 class="services-title">Comprehensive Workforce Solutions</h2>
<p class="services-lead">From healthcare to heavy industry, we provide skilled professionals across all major sectors, with specialized expertise in government contracting and compliance.</p>

<div class="service-grid">
  <article class="service"><div class="ico"><svg width="15" height="15" viewBox="0 0 24 24" fill="none" stroke="#1d5cf5" stroke-width="2"><path d="M12 20s-8-5-8-11a4.5 4.5 0 0 1 8-2.5A4.5 4.5 0 0 1 20 9c0 6-8 11-8 11z"/></svg></div>
    <h3>Healthcare</h3><p>Certified medical professionals, nurses, and healthcare support staff for hospitals and clinics.</p>
    <ul><li>Licensed Professionals</li><li>Emergency Staffing</li><li>Long-term Placements</li></ul></article>
  <article class="service"><div class="ico"><svg width="15" height="15" viewBox="0 0 24 24" fill="none" stroke="#1d5cf5" stroke-width="2"><rect x="3" y="4" width="18" height="12" rx="1"/><path d="M8 20h8M12 16v4"/></svg></div>
    <h3>Information Technology</h3><p>Skilled IT professionals, developers, and technical specialists for digital transformation.</p>
    <ul><li>Software Development</li><li>Cybersecurity</li><li>Cloud Solutions</li></ul></article>
  <article class="service"><div class="ico"><svg width="15" height="15" viewBox="0 0 24 24" fill="none" stroke="#1d5cf5" stroke-width="2"><path d="M3 6h11v10H3zM14 10h4l3 3v3h-7z"/><circle cx="7" cy="17" r="2"/><circle cx="17" cy="17" r="2"/></svg></div>
    <h3>Logistics</h3><p>Supply chain experts, warehouse workers, and transportation professionals.</p>
    <ul><li>Supply Chain Management</li><li>Warehouse Operations</li><li>Transportation</li></ul></article>
  <article class="service"><div class="ico"><svg width="15" height="15" viewBox="0 0 24 24" fill="none" stroke="#1d5cf5" stroke-width="2"><path d="M15 4a5 5 0 0 0-5 6.5L3.5 17a2 2 0 0 0 3 3L13 13.5A5 5 0 0 0 20 9l-3 1-3-3 1-3z"/></svg></div>
    <h3>Maintenance</h3><p>Experienced maintenance technicians and facilities management professionals.</p>
    <ul><li>Preventive Maintenance</li><li>Emergency Repairs</li><li>Facilities Management</li></ul></article>
  <article class="service"><div class="ico"><svg width="15" height="15" viewBox="0 0 24 24" fill="none" stroke="#1d5cf5" stroke-width="2"><path d="M3 18h18v2H3zM5 18a7 7 0 0 1 14 0M10 11V7h4v4"/></svg></div>
    <h3>Construction</h3><p>Licensed contractors, project managers, and construction workers for all project sizes.</p>
    <ul><li>Project Management</li><li>Skilled Trades</li><li>Safety Compliance</li></ul></article>
  <article class="service"><div class="ico"><svg width="15" height="15" viewBox="0 0 24 24" fill="none" stroke="#1d5cf5" stroke-width="2"><path d="M3 21V8l5 3V8l5 3V4h4l1 17z"/><path d="M8 16h1M12 16h1M16 16h1"/></svg></div>
    <h3>Manufacturing</h3><p>Production workers, quality control specialists, and manufacturing engineers.</p>
    <ul><li>Production Line</li><li>Quality Assurance</li><li>Process Optimization</li></ul></article>
  <article class="service"><div class="ico"><svg width="15" height="15" viewBox="0 0 24 24" fill="none" stroke="#1d5cf5" stroke-width="2"><circle cx="12" cy="12" r="3"/><path d="M12 2v3M12 19v3M2 12h3M19 12h3M5 5l2 2M17 17l2 2M5 19l2-2M17 7l2-2"/><circle cx="12" cy="12" r="7"/></svg></div>
    <h3>Industrial</h3><p>Heavy industry professionals and specialized technical workers.</p>
    <ul><li>Heavy Machinery</li><li>Safety Protocols</li><li>Technical Expertise</li></ul></article>
  <article class="service"><div class="ico"><svg width="15" height="15" viewBox="0 0 24 24" fill="none" stroke="#1d5cf5" stroke-width="2"><circle cx="9" cy="8" r="3.5"/><path d="M2 20a7 7 0 0 1 14 0M16 4.5a3.5 3.5 0 0 1 0 7M18 14a6 6 0 0 1 4 6"/></svg></div>
    <h3>General Labor</h3><p>Reliable general laborers for temporary and permanent positions across industries.</p>
    <ul><li>Flexible Scheduling</li><li>Background Verified</li><li>Immediate Availability</li></ul></article>
</div>

<section class="gov-band">
  <h2>Government Contracting Expertise</h2>
  <p>As a certified VOSB, SDVOSB, DBE, and Minority-Owned Business, we specialize in government contracts and understand the unique requirements of federal, state, and local agencies.</p>
  <div class="gov-btn">View Our Capabilities
    <svg width="7" height="7" viewBox="0 0 24 24" fill="none" stroke="#1d5cf5" stroke-width="2.5"><path d="M4 12h15M13 6l6 6-6 6"/></svg></div>
</section>
</body>
</html>
```